1page Pre-launch landing page for Machine Learning startup

We need a 1page pre-launch landing page that (1) provides information on what we are building (2) core benefits and (3) email signup . Our company, Copper Lantern Labs, is building a Machine Learning service that makes using Machine learning so easy, any business person without technical expertise can easily use to solve their business problems.
Target Market(s)
MBAs or business people in organizations who want to test, use and maybe deploy machine learning solutions in their busines.
Industry/Entity Type
Machine Learning
Requirements
Must have
- Newsletter signup section. Link to an alpha version of the product (for small group of people participating as alpha testers)
Nice to have
- "machine learning for the rest of us"
- "machine learning SO easy, an MBA can use"
- 'test and use Machine learning solutions without knowing data science or hiring expensive data scientists.
- "I wouldn't be seen dead using this - Data Scientst, Ph.D"

```html
<!DOCTYPE html>
<html lang="en">
<head>
<meta charset="utf-8">
<title>Copper Lantern Labs — Machine Learning for the Rest of Us</title>
<link href="https://fonts.googleapis.com/css2?family=Montserrat:wght@400;500;600;700&display=swap" rel="stylesheet">
<style>
:root{
  --blue:#0a6fe8;
  --blue-deep:#0055d4;
  --blue-light:#1aa3f0;
  --sky:#e6f0fd;
  --green:#22c76b;
  --green-light:#21d37e;
  --ink:#1d1d2b;
  --muted:#7a7f8c;
  --line:#e7eaef;
  --white:#ffffff;
}
*{box-sizing:border-box;margin:0;padding:0}
html,body{width:1200px;height:1200px;overflow:hidden;background:var(--white)}
body{font-family:"Montserrat",sans-serif;color:var(--ink);position:relative}
.page{position:absolute;left:432px;top:0;width:420px;height:1500px;transform:scale(.8);transform-origin:0 0;background:var(--white);box-shadow:0 0 6px rgba(0,0,0,.08)}
.abs{position:absolute}

/* nav */
.nav{left:0;top:0;width:420px;height:24px;background:var(--white)}
.brand{left:52px;top:3px;display:flex;flex-direction:column;align-items:center}
.brand-dot{width:10px;height:10px;border:1.2px solid var(--blue);border-radius:50%}
.brand-name{font-size:5px;font-weight:500;color:var(--blue);margin-top:1px;white-space:nowrap}
.nav-links{left:146px;top:10px;display:flex;gap:13px;font-size:4.2px;color:var(--muted)}
.nav-cta{left:289px;top:8px;width:56px;height:9px;border-radius:5px;background:var(--blue);color:var(--white);font-size:3.8px;font-weight:600;display:flex;align-items:center;justify-content:center}
.nav-login{left:350px;top:10px;font-size:4.2px;color:var(--blue)}

/* hero */
.hero{left:0;top:24px;width:420px;height:194px;overflow:hidden;background:linear-gradient(135deg,#f3f8ff,var(--sky))}
.hero-blob{left:0;top:0}
.hero-art{left:228px;top:24px;width:134px;height:144px;border-radius:50% 45% 42% 48%;background:radial-gradient(circle at 40% 45%,#29c4f0 0,#1e6fe0 55%,rgba(30,111,224,.15) 75%,transparent 76%)}
.hero-title{left:52px;top:44px;width:150px;color:var(--white);font-size:8.6px;font-weight:700;line-height:12.5px}
.hero-text{left:52px;top:74px;width:150px;color:var(--white);font-size:4.3px;font-weight:500;line-height:8px}
.btn-green{left:52px;top:114px;width:53px;height:15px;background:var(--green);color:var(--white);font-size:4.3px;font-weight:700;display:flex;align-items:center;justify-content:center}

/* intro */
.section-title{width:420px;left:0;text-align:center;font-size:11.5px;font-weight:500;color:var(--ink)}
.intro-text{left:80px;top:286px;width:260px;text-align:center;font-size:5.3px;line-height:9px;color:var(--muted)}
.feature{top:321px;width:74px;text-align:center}
.feature-ring{width:34px;height:34px;margin:0 auto;border:1.3px solid var(--blue-light);border-radius:50%;display:flex;align-items:center;justify-content:center}
.feature-art{width:24px;height:24px;border-radius:50%;background:radial-gradient(circle,#8e96a6,#5d6575)}
.feature-name{font-size:4.6px;font-weight:600;margin-top:9px}
.feature-text{font-size:3.5px;line-height:7px;color:var(--muted);margin-top:3px}

/* building */
.build-title{left:52px;top:421px;font-size:12px;font-weight:500;color:#0b3c73}
.build-title span{color:var(--blue-light)}
.photo-lab{left:52px;top:449px;width:178px;height:118px;background:linear-gradient(160deg,#e6e8f4,#8a8fb3 50%,#3b3f63)}
.photo-code{left:188px;top:559px;width:178px;height:118px;background:linear-gradient(120deg,#0f2a5c,#2f5f9c 40%,#8a8d95 70%,#b0603a)}
.copy{font-size:3.5px;line-height:7.3px;color:var(--muted)}
.copy p+p{margin-top:6px}

/* quote */
.quote{left:0;top:722px;width:420px;height:93px;background:linear-gradient(90deg,var(--green),var(--green-light));color:var(--white);text-align:center}
.quote-text{margin-top:32px;font-size:10.5px;font-weight:500}
.quote-by{margin-top:4px;font-size:4.8px;opacity:.85}

/* benefits */
.benefit-card{width:80px;height:91px;background:var(--white);box-shadow:0 1px 5px rgba(0,0,0,.22);display:flex;align-items:center;justify-content:center}
.benefit-art{width:60px;height:62px;border-radius:8px}
.benefit-num{width:13px;height:13px;border-radius:50%;background:var(--blue-light);color:var(--white);font-size:4px;font-weight:700;display:flex;align-items:center;justify-content:center}
.benefit-title{font-size:7.6px;font-weight:600;white-space:nowrap}
.benefit-text{width:100px;font-size:3.4px;line-height:7.3px;color:var(--muted)}
.right{text-align:right}

/* footer */
.footer{left:0;top:1376px;width:420px;height:101px;background:linear-gradient(90deg,var(--blue-deep),var(--blue-light));color:var(--white)}
.footer-dot{left:201px;top:14px;width:18px;height:18px;border:1.5px solid var(--white);border-radius:50%}
.footer-name{left:0;top:34px;width:420px;text-align:center;font-size:5.5px;font-weight:500}
.signup{left:139px;top:51px;width:141px;height:18px;display:flex}
.signup-input{flex:1;background:var(--white);color:#555;font-size:3.6px;display:flex;align-items:center;padding-left:7px}
.signup-btn{width:21px;background:var(--green);display:flex;align-items:center;justify-content:center}
.social{left:167px;top:77px;display:flex;gap:2px}
.social i{width:20px;height:10px;background:var(--green-light)}
.legal{left:0;top:1487px;width:420px;text-align:center;font-size:3.6px;color:#444}
</style>
</head>
<body>
<div class="page">

  <header class="abs nav">
    <div class="abs brand"><div class="brand-dot"></div><div class="brand-name">Copper Lantern Labs</div></div>
    <nav class="abs nav-links"><span>Home</span><span>About Us</span><span>What we are Building</span><span>Benefits</span></nav>
    <div class="abs nav-cta">Request access to Alpha</div>
    <div class="abs nav-login">Login</div>
  </header>

  <section class="abs hero">
    <svg class="abs hero-blob" width="220" height="194" viewBox="0 0 220 194">
      <defs><linearGradient id="heroBlue" x1="0" y1="0" x2="1" y2="1"><stop offset="0" stop-color="#0a7af0"/><stop offset="1" stop-color="#0057d8"/></linearGradient></defs>
      <path d="M0 0 H185 C200 40 225 110 210 165 C200 195 175 196 150 186 C100 166 50 152 0 162 Z" fill="url(#heroBlue)"/>
    </svg>
    <div class="abs hero-art" role="img" aria-label="Brain illustration with connected nodes"></div>
    <h1 class="abs hero-title">Machine Learning SO Easy, An MBA Can Use</h1>
    <p class="abs hero-text">Test and use machine learning solutions without knowing data science or hiring expensive data scientists. Upload your business data, pick a goal, and see results in minutes.</p>
    <div class="abs btn-green">Get Started</div>
  </section>

  <h2 class="abs section-title" style="top:262px">Machine Learning For The Rest Of Us</h2>
  <p class="abs intro-text">Simple tools that turn your everyday business data into clear predictions. No code, no lab coats, just answers you can act on.</p>

  <div class="abs feature" style="left:99px">
    <div class="feature-ring"><div class="feature-art" role="img" aria-label="Deep learning icon"></div></div>
    <div class="feature-name">Deep Learning</div>
    <div class="feature-text">Layered models find patterns in your data without any manual tuning at all.</div>
  </div>
  <div class="abs feature" style="left:173px">
    <div class="feature-ring"><div class="feature-art" role="img" aria-label="Algorithm icon"></div></div>
    <div class="feature-name">Algorithm</div>
    <div class="feature-text">We choose the right method for each problem so you can focus on decisions.</div>
  </div>
  <div class="abs feature" style="left:248px">
    <div class="feature-ring"><div class="feature-art" role="img" aria-label="Neural networks icon"></div></div>
    <div class="feature-name">Neural Networks</div>
    <div class="feature-text">Connected models learn from results and improve with every new record added.</div>
  </div>

  <h2 class="abs build-title">What We <span>Are Building?</span></h2>
  <div class="abs photo-lab" role="img" aria-label="Photo of a modern hospital operating room"></div>
  <div class="abs copy" style="left:235px;top:449px;width:132px">
    <p>We are building a service that lets any business person ask real questions of their data. Connect a spreadsheet or database, describe the outcome you care about, and our platform prepares the data, trains several models and explains which one works best and why, in plain language that fits a board slide.</p>
    <p>Healthcare teams can forecast bed demand, retailers can predict churn, and finance groups can flag risky invoices, all without writing a single line of code or waiting on a data team.</p>
  </div>
  <div class="abs copy" style="left:52px;top:576px;width:128px">
    <p>Behind the simple screens sits a careful engine that checks data quality, guards against overfitting and keeps every experiment versioned. You see clear charts, confidence ranges and suggested next steps instead of raw math, so teams can trust results and share them across the company.</p>
    <p>When a model proves useful you can deploy it with one click, schedule fresh predictions and watch performance over time, with alerts when things drift from expected.</p>
  </div>
  <div class="abs photo-code" role="img" aria-label="Photo of a laptop showing code beside a coffee mug"></div>

  <section class="abs quote">
    <p class="quote-text">“I wouldn't be seen dead using this”</p>
    <p class="quote-by">- Data Scientist, Ph.D</p>
  </section>

  <h2 class="abs section-title" style="top:844px">Core Benefits</h2>

  <div class="abs benefit-num" style="left:209px;top:889px">1.</div>
  <div class="abs benefit-title right" style="left:100px;top:909px;width:120px">Praesent Iaculis Nunc</div>
  <div class="abs benefit-text right" style="left:120px;top:922px">Plain answers from your data, ready to share with your team today.</div>
  <div class="abs benefit-card" style="left:247px;top:884px"><div class="benefit-art" role="img" aria-label="Chip with brain illustration" style="background:radial-gradient(circle,#3fd0c0,#1a2a3a 60%,#fff 62%)"></div></div>

  <div class="abs benefit-card" style="left:121px;top:1007px"><div class="benefit-art" role="img" aria-label="Network brain illustration" style="background:radial-gradient(circle,#d24a6a,#3aa08a 55%,#fff 70%)"></div></div>
  <div class="abs benefit-num" style="left:226px;top:1012px">2.</div>
  <div class="abs benefit-title" style="left:226px;top:1032px">Praesent Iaculis Nunc</div>
  <div class="abs benefit-text" style="left:226px;top:1045px">No data scientist needed to test, train and compare models quickly.</div>

  <div class="abs benefit-num" style="left:209px;top:1135px">3.</div>
  <div class="abs benefit-title right" style="left:100px;top:1155px;width:120px">Praesent Iaculis Nunc</div>
  <div class="abs benefit-text right" style="left:120px;top:1168px">Clear results explained in business terms, never in dense formulas.</div>
  <div class="abs benefit-card" style="left:247px;top:1130px"><div class="benefit-art" role="img" aria-label="Gear and brain illustration" style="background:linear-gradient(90deg,#e04848 50%,#f2b638 50%)"></div></div>

  <div class="abs benefit-card" style="left:121px;top:1253px"><div class="benefit-art" role="img" aria-label="Chip inside house illustration" style="background:linear-gradient(180deg,#e03434 35%,#d9dde2 35%,#2f3a44)"></div></div>
  <div class="abs benefit-num" style="left:226px;top:1258px">4.</div>
  <div class="abs benefit-title" style="left:226px;top:1278px">Praesent Iaculis Nunc</div>
  <div class="abs benefit-text" style="left:226px;top:1291px">Deploy winning models in one click and track them over time.</div>

  <footer class="abs footer">
    <div class="abs footer-dot"></div>
    <div class="abs footer-name">Copper Lantern Labs</div>
    <div class="abs signup">
      <div class="signup-input">Enter Your Mail Id</div>
      <div class="signup-btn">
        <svg width="8" height="8" viewBox="0 0 10 10"><path d="M0 4.5 L10 0 L6 10 L4.5 6 Z" fill="#fff"/></svg>
      </div>
    </div>
    <div class="abs social"><i></i><i></i><i></i><i></i></div>
  </footer>
  <p class="abs legal">© 2018 Copper Lantern Labs. All Rights Reserved | Privacy Policy</p>

</div>
</body>
</html>
```